Adventurous female pilot

I am looking for a personal business card, for a very well qualified female pilot, with a lot of aviation experience.

Currently an airline pilot, have worked as a bush pilot in Africa, looking to get into corporate aviation, or private jet owners.
Want a classy looking card for networking...

Could be interested in a retro\vintage look also?!

An idea,, is an african sunset background, with my wings\logo on it
Updates

I just want to say thank you to all of your for your amazing designs!

I have been very busy flying this past week , so not had a chance to be on the computer much.
But I provide some feedback, and conclusions very soon!
Thank you again.

Marla

Reason: Still waiting on a couple of revisions to be 100% about my choice!

Target Market(s)

corporate aviation, private jet owners, casino's,
General audience.
networking

Industry/Entity Type

Airline

Requirements
Nice to have
• Classy, edgy, sexy, but also feminine

```html
<!DOCTYPE html>
<html lang="en">
<head>
<meta charset="utf-8">
<title>Marla Hale Aviation – Business Card</title>
<link href="https://fonts.googleapis.com/css2?family=Pinyon+Script&family=Tinos&family=PT+Sans&display=swap" rel="stylesheet">
<style>
  :root {
    --orange-deep: #ff6a00;
    --orange-mid: #ff9a12;
    --yellow-warm: #ffc928;
    --yellow-pale: #ffe9a0;
    --title-yellow: #ffff2e;
    --white: #ffffff;
    --ink-grey: #2a2a2a;
    --map-tone: rgba(255, 236, 170, 0.35);
    --plane-light: #f7dca8;
    --plane-dark: #c99a5a;
  }
  html, body {
    margin: 0;
    padding: 0;
    width: 1200px;
    height: 686px;
    overflow: hidden;
    background: var(--white);
  }
  .card {
    position: relative;
    width: 1200px;
    height: 686px;
    overflow: hidden;
    background: linear-gradient(200deg, var(--yellow-pale) 0%, var(--yellow-warm) 30%, var(--orange-mid) 60%, var(--orange-deep) 100%);
  }
  .card-shapes {
    position: absolute;
    inset: 0;
  }
  .brand-mark {
    position: absolute;
    left: 120px;
    top: 150px;
    display: flex;
    align-items: center;
    gap: 14px;
    font-family: "PT Sans", sans-serif;
    font-size: 26px;
    line-height: 1.15;
    color: var(--ink-grey);
    letter-spacing: 1px;
  }
  .brand-mark .dot {
    width: 22px;
    height: 22px;
    border-radius: 50%;
    background: var(--ink-grey);
    flex: none;
  }
  .card-title {
    position: absolute;
    left: 230px;
    top: 248px;
    margin: 0;
    font-family: "Pinyon Script", cursive;
    font-weight: 400;
    font-size: 112px;
    line-height: 1;
    color: var(--title-yellow);
    white-space: nowrap;
  }
  .card-subtitle {
    position: absolute;
    left: 646px;
    top: 404px;
    margin: 0;
    font-family: "Tinos", serif;
    font-size: 40px;
    letter-spacing: 2px;
    color: var(--yellow-pale);
  }
  .contact {
    position: absolute;
    margin: 0;
    color: var(--white);
    white-space: nowrap;
  }
  .contact-phone {
    font-family: "PT Sans", sans-serif;
    font-size: 40px;
  }
  .contact-phone.us { left: 88px; top: 466px; }
  .contact-phone.taipei { left: 55px; top: 524px; }
  .contact-email {
    left: 28px;
    top: 622px;
    font-family: "Tinos", serif;
    font-size: 43px;
  }
</style>
</head>
<body>
<main class="card">
  <svg class="card-shapes" width="1200" height="686" viewBox="0 0 1200 686" aria-hidden="false">
    <defs>
      <linearGradient id="planeTone" x1="0" y1="0" x2="0" y2="1">
        <stop offset="0" stop-color="var(--plane-light)"/>
        <stop offset="1" stop-color="var(--plane-dark)"/>
      </linearGradient>
      <radialGradient id="floralTone" cx="0.6" cy="0.5" r="0.6">
        <stop offset="0" stop-color="#ff8a1a"/>
        <stop offset="0.5" stop-color="#ffd27a"/>
        <stop offset="1" stop-color="#fff6dc"/>
      </radialGradient>
    </defs>

    <path class="world-map" role="img" aria-label="Faint world map in the background"
          d="M160,300 C220,250 330,260 420,300 C480,230 560,180 640,170 C700,90 860,40 1000,60 C1080,80 1100,150 1060,220 C1010,270 900,280 820,260 C760,330 700,360 640,350 C560,420 480,520 380,560 C320,500 280,420 220,380 C180,360 150,330 160,300 Z"
          fill="var(--map-tone)"/>

    <path class="corner-sweep" d="M0,0 H620 C540,50 490,190 410,240 C300,280 130,255 0,265 Z" fill="var(--white)"/>

    <path class="side-sweep" d="M1200,228 C1160,236 1140,300 1150,362 C1060,420 1036,560 1078,686 H1200 Z" fill="var(--white)"/>

    <path class="floral-ornament" role="img" aria-label="White floral swirl ornament with orange glow"
          d="M1200,330 C1120,340 1060,390 1050,450 C1000,480 950,520 940,600 C980,640 1040,660 1120,640 C1160,600 1200,560 1200,520 Z"
          fill="url(#floralTone)" opacity="0.9"/>

    <ellipse class="aircraft" role="img" aria-label="Twin-engine turboprop aircraft illustration"
             cx="880" cy="528" rx="250" ry="72" fill="url(#planeTone)" opacity="0.9"/>
  </svg>

  <div class="brand-mark">
    <span class="dot"></span>
    <span>MARLA HALE<br>AVIATION</span>
  </div>

  <h1 class="card-title">Marla Hale</h1>
  <p class="card-subtitle">AVIATION</p>

  <p class="contact contact-phone us">Cell US: +1 702-555-0148</p>
  <p class="contact contact-phone taipei">Cell Taipei: +886 970-555-208</p>
  <p class="contact contact-email">Email: marlahale@skymail.com</p>
</main>
</body>
</html>
```